Doctor to Patient Management Website

I need a design for a health management website that connects doctors to patients. The website will consist of: A main page mainly describing our goal, services, and initiatives towards (Who we are AKA "About Us", Our services, Contact Us, Quick Links for health tips, Language selection, Find a doctor, search bar, Member Login Section, small glossary section below with links to all entities mentioned prior, Help section (Helpful tips and tutorials, Used to request help from admin, customer service, to resolve issues or get assistance). A profile page with two types:1) Doctor Profile: Doctor Personal info (First, Last, Middle Name, Title), Clinic, Hospital Info, Department, Credentials, Years of Experience, Patients rating, #Patients seen during the current week, #Patients seen in total, Picture, Link to email doctor, Link to print doctor's profile). Tabs for "About Me", "Contact Info", "Ratings & Comments", "Documents" (To be downloaded and uploaded by patient), "Patients (List of Patients alphabetical order by name)", "Calendar" (to see doctor's availability for booking) underneath all links. 2) Patient profile: About me, Personal Info, Height, Weight, Blood Type, Age, DOB, Name, etc..., Message and email link.Picture of patient with menu made of "Personal Data", "Biometrics", "Allergies", "Illnesses", "Medications", "Medical Procedures", "Doctors" treating the patient, "Documents" (To be downloaded and uploaded by patient). Underneath all, other patients he or she is related to (For example: family member, so patient can't connect to other patients who are family members)3) Login section: New Users will have option to register using:First Name (Required), Last Name, Middle (not required), Address (Not required), City (Required), Country (Required), Email (Not required), Phone Number (Required), Choose UserName, Password, Account Type (Doctor or Patient). Once registered, they will log in using UserName, Password, and Account_Type.Curent Users will log in using UserName, Password, and Account_Type and option to retrieve username or password.Pages to include (Login Page - Registration Page - Retrieve Username and Reset Password Page)Please see link below:https://lanternpost-media.example/importance-claiming-vitalrank-quopa-zeltra/Pictures are attached to this project as an inspirationFYI: Dummy text can be used to fill in the business, services, and descriptive information. Feel free to include your own ideas in the layout, design, categories, patterns, and more to and showcase your talent. Design and pictures provided are available as source of ideas.

Target Market(s)

Age: 21+ / Family Oriented / Medical Sector / Metropolitan Area / Educated and non Educated Users

Industry/Entity Type

Health Care

Number of Pages Required

5+ page

Font styles to use
Sans Serif

Colors

Designer to choose colors to be used in the design.

Requirements
Must have
• Thin layer design
• Simple font - No serif
• Clean menu with light but solid colors (No Gradient effect)
Nice to have
• Different color themes (2 or 3) can be combined
• Sample pictures for illustration (either as an ad or to go with the flow of your design)
• Dashboard Feel (Suggested but not required)
Should not have
• Artistic fonts - with Serif
• Dark color themes

```html
<!DOCTYPE html>
<html lang="en">
<head>
<meta charset="utf-8">
<title>Carevia – Find a Doctor</title>
<link rel="stylesheet" href="https://fonts.googleapis.com/css2?family=Montserrat:wght@400;500;600;700;800&display=swap">
<style>
:root{
  --purple:#4a3d8f;
  --purple-dark:#3a2f73;
  --teal:#4fc3b4;
  --teal-dark:#3aa99b;
  --red:#e5534b;
  --ink:#2d2d3a;
  --muted:#8a8a99;
  --line:#e6e6ee;
  --soft:#f6f6fa;
  --white:#ffffff;
  --footer-bar:#2f2a55;
}
*{box-sizing:border-box;margin:0;padding:0}
html,body{width:1200px;height:2904px;overflow:hidden}
body{font-family:'Montserrat',sans-serif;color:var(--ink);background:var(--white);font-size:14px}
.btn{display:inline-block;background:var(--teal);color:var(--white);font-weight:600;font-size:13px;padding:12px 28px;border-radius:3px;text-decoration:none}
.accent{color:var(--teal)}
.section-title{font-size:30px;font-weight:500;text-align:center;letter-spacing:.5px}
.section-title strong{font-weight:800}
.section-lead{max-width:560px;margin:12px auto 0;text-align:center;color:var(--muted);font-size:13px;line-height:1.6}

/* header */
.site-header{height:80px;padding:0 100px;display:flex;align-items:center;justify-content:space-between;position:relative}
.brand{display:flex;align-items:center;gap:8px;font-weight:700;font-size:20px;color:var(--ink);letter-spacing:1px}
.brand-square{width:24px;height:24px;background:var(--ink)}
.utility-nav{position:absolute;top:8px;right:100px;display:flex;gap:6px}
.utility-nav span{background:var(--red);color:var(--white);font-size:10px;padding:3px 12px;border-radius:2px}
.main-nav{display:flex;gap:36px;align-items:center;margin-top:18px;font-size:13px}
.main-nav a{color:var(--ink);text-decoration:none}
.main-nav .btn{padding:7px 18px;font-size:12px}

/* hero */
.hero{height:480px;background:var(--purple);position:relative;color:var(--white);text-align:center;padding-top:90px}
.hero-art{position:absolute;top:0;height:100%;width:330px;background:linear-gradient(135deg,#5a4da0,#463a88)}
.hero-art.left{left:0}.hero-art.right{right:0}
.hero h1{font-size:44px;font-weight:800;letter-spacing:1px;position:relative}
.hero p{max-width:420px;margin:12px auto 0;font-size:13px;line-height:1.6;opacity:.85;position:relative}
.search-bar{position:relative;width:500px;margin:34px auto 0;display:flex;background:var(--white);border-radius:3px;overflow:hidden}
.search-bar span{flex:1;text-align:left;padding:14px 16px;color:var(--muted);font-size:12px}
.search-bar b{background:var(--teal);padding:14px 28px;font-size:12px;font-weight:600}
.filter-tabs{position:relative;display:flex;justify-content:center;gap:8px;margin-top:22px}
.filter-tabs span{font-size:11px;padding:6px 18px;background:var(--purple-dark);border-radius:2px}
.filter-tabs span.active{background:var(--teal)}

/* appointment */
.appointment{height:560px;padding-top:56px;text-align:center}
.steps{display:flex;justify-content:center;align-items:center;gap:18px;margin-top:44px}
.step-card{width:240px;height:240px;background:var(--white);box-shadow:0 4px 18px rgba(40,40,80,.12);padding:40px 26px;text-align:left}
.step-card svg{display:block;margin:0 auto 22px}
.step-card h3{font-size:17px;font-weight:600;text-align:center;margin-bottom:14px}
.step-card p{font-size:12px;color:var(--muted);line-height:1.6}
.step-arrow{color:var(--teal)}
.appointment .btn{margin-top:40px}

/* about */
.about{height:400px;background:var(--soft);display:flex;align-items:center;padding:0 100px;gap:60px}
.about-art{width:500px;height:290px;border-radius:6px;background:linear-gradient(135deg,#c6d9f1,#e8e3f3)}
.about-copy{flex:1}
.about-copy h2{font-size:32px;font-weight:500;margin-bottom:18px}
.about-copy h2 strong{font-weight:800}
.about-copy p{font-size:12px;color:var(--muted);line-height:1.7;margin-bottom:12px}

/* testimonial + login */
.testimonial{height:500px;position:relative;background:linear-gradient(120deg,#3d3f52,#5b6275 60%,#474b5e);color:var(--white);display:flex;padding:60px 100px;gap:80px}
.quote{width:440px}
.quote h2{font-size:34px;font-weight:800;line-height:1.2}
.quote-mark{font-size:56px;color:var(--teal);line-height:1;margin-top:24px;font-weight:800}
.quote p{font-size:13px;line-height:1.7;opacity:.9;margin-top:-10px}
.author{text-align:center;margin-top:26px}
.avatar{width:64px;height:64px;border-radius:50%;background:linear-gradient(135deg,#e0b49c,#b9876d);margin:0 auto 10px;border:3px solid var(--white)}
.author b{font-size:14px;letter-spacing:1px}
.dots{display:flex;justify-content:center;gap:6px;margin-top:10px}
.dots i{width:7px;height:7px;border-radius:50%;background:rgba(255,255,255,.5)}
.dots i:first-child{background:var(--white)}
.login-panel{width:420px;height:380px;border:2px solid rgba(255,255,255,.8);background:rgba(30,30,45,.35);padding:0 40px 30px}
.tabs{display:flex;margin:0 -40px 30px}
.tabs span{flex:1;text-align:center;padding:14px;font-size:15px;border-bottom:1px solid rgba(255,255,255,.4)}
.tabs span.active{background:var(--teal)}
.field{background:var(--white);color:var(--ink);font-size:12px;padding:12px 14px;margin-bottom:14px;border-radius:2px;display:flex;justify-content:space-between}
.login-panel .btn{display:block;width:150px;margin:26px 0 0 auto;text-align:center}

/* doctors */
.doctors{height:560px;padding-top:50px;text-align:center;position:relative}
.doctor-row{display:flex;justify-content:center;gap:24px;margin-top:34px;position:relative}
.doctor-card{width:300px;background:var(--white);box-shadow:0 4px 18px rgba(40,40,80,.12);text-align:left}
.doctor-photo{height:190px;background:linear-gradient(135deg,#dfe9f2,#b9cadb)}
.doctor-info{padding:16px 20px}
.doctor-info h3{font-size:14px;font-weight:700}
.doctor-info small{display:block;font-size:10px;color:var(--muted);margin:4px 0 10px}
.rating{display:flex;justify-content:space-between;font-size:10px;color:var(--muted)}
.stars{color:#f5a623;font-size:14px;letter-spacing:2px}
.slider-arrow{position:absolute;top:100px;font-size:22px;color:var(--muted)}
.doctors .btn{margin-top:34px}

/* footer */
.social-bar{height:60px;background:var(--purple);color:var(--white);display:flex;align-items:center;justify-content:space-between;padding:0 100px;font-size:13px}
.social-bar div{display:flex;gap:30px}
.social-bar i{width:18px;height:18px;border-radius:50%;background:rgba(255,255,255,.85)}
.site-footer{height:208px;background:var(--teal);display:flex;align-items:center;padding:0 100px;color:var(--white)}
.site-footer .brand{color:var(--white);width:300px}
.site-footer .brand-square{background:var(--white)}
.footer-col{flex:1;text-align:center;font-size:12px;line-height:1.6}
.footer-col h4{font-size:15px;font-weight:700;letter-spacing:1px;margin:6px 0}
.legal-bar{height:56px;background:var(--footer-bar);color:rgba(255,255,255,.7);display:flex;align-items:center;justify-content:space-between;padding:0 100px;font-size:11px}
.legal-bar nav{display:flex;gap:20px}
</style>
</head>
<body>

<header class="site-header">
  <div class="brand"><span class="brand-square"></span>CAREVIA</div>
  <div class="utility-nav"><span>Language</span><span>Help</span><span>Contact</span></div>
  <nav class="main-nav">
    <a href="#">Home</a><a href="#">About Us</a><a href="#">Our Services ▾</a><a href="#">Health Tips ▾</a>
    <a href="#">Login</a><a class="btn" href="#">Sign Up</a>
  </nav>
</header>

<section class="hero">
  <div class="hero-art left" role="img" aria-label="Illustration of a stethoscope, pills and medical supplies"></div>
  <div class="hero-art right" role="img" aria-label="Illustration of a clipboard, syringe and medicine bottles"></div>
  <h1>FIND A DOCTOR</h1>
  <p>Lorem ipsum dolor sit amet, at placerat ligula nec mattis. Vivamus quis, tincidunt mollis, mauris massa porttitor feugiat.</p>
  <div class="search-bar"><span>Search by name, specialty or clinic</span><b>SEARCH</b></div>
  <div class="filter-tabs"><span class="active">All</span><span>Clinics</span><span>Doctors</span></div>
</section>

<section class="appointment">
  <h2 class="section-title">DISCOVER THE <strong class="accent">ONLINE</strong> APPOINTMENT!</h2>
  <p class="section-lead">Lorem ipsum dolor sit amet, at placerat ligula nec mattis, in consequat sapien. Vivamus quis, tincidunt mollis, mauris massa porttitor feugiat.</p>
  <div class="steps">
    <div class="step-card">
      <svg width="40" height="40" viewBox="0 0 40 40" fill="none" stroke="#4fc3b4" stroke-width="3"><circle cx="17" cy="17" r="11"/><path d="M25 25l10 10" stroke="#e5534b"/></svg>
      <h3>Find A Doctor</h3>
      <p>Lorem ipsum dolor sit amet, at placerat ligula nec mattis, vivamus quis tincidunt mollis mauris.</p>
    </div>
    <svg class="step-arrow" width="24" height="24" viewBox="0 0 24 24" fill="none" stroke="currentColor" stroke-width="2.5"><path d="M4 12h15M13 6l6 6-6 6"/></svg>
    <div class="step-card">
      <svg width="44" height="40" viewBox="0 0 44 40" fill="none" stroke="#2d2d3a" stroke-width="3"><path d="M2 20c6-10 14-14 20-14s14 4 20 14c-6 10-14 14-20 14S8 30 2 20z"/><circle cx="22" cy="20" r="6" fill="#4fc3b4"/></svg>
      <h3>View Profile</h3>
      <p>Lorem ipsum dolor sit amet, at placerat ligula nec mattis, vivamus quis tincidunt mollis mauris.</p>
    </div>
    <svg class="step-arrow" width="24" height="24" viewBox="0 0 24 24" fill="none" stroke="currentColor" stroke-width="2.5"><path d="M4 12h15M13 6l6 6-6 6"/></svg>
    <div class="step-card">
      <svg width="36" height="40" viewBox="0 0 36 40" fill="none" stroke="#2d2d3a" stroke-width="3"><rect x="3" y="5" width="30" height="33" rx="2"/><rect x="11" y="2" width="14" height="6" fill="#e5534b" stroke="none"/><path d="M10 18l4 4 8-8M10 30h16" stroke="#4fc3b4"/></svg>
      <h3>Book A Visit</h3>
      <p>Lorem ipsum dolor sit amet, at placerat ligula nec mattis, vivamus quis tincidunt mollis mauris.</p>
    </div>
  </div>
  <a class="btn" href="#">View All</a>
</section>

<section class="about">
  <div class="about-art" role="img" aria-label="Illustration of a doctor and a family seated on a sofa with a speech bubble"></div>
  <div class="about-copy">
    <h2>ABOUT <strong class="accent">US</strong></h2>
    <p>Lorem ipsum dolor sit amet, at placerat ligula nec mattis, in consequat sapien. Vivamus quis tincidunt mollis, mauris massa porttitor feugiat, ut sodales nibh lorem non nunc. Donec gravida libero sed nisi elementum tempus.</p>
    <p>Nulla facilisi. Integer commodo velit at arcu dictum, sit amet pretium orci feugiat. Aenean vitae erat quis enim faucibus convallis ac nec augue.</p>
    <a class="btn" href="#">Read More</a>
  </div>
</section>

<section class="testimonial" role="img" aria-label="Blurred background photograph of a clinic workspace">
  <div class="quote">
    <h2>DONT TAKE OUR WORD<br>FOR IT !</h2>
    <div class="quote-mark">“</div>
    <p>Lorem ipsum dolor sit amet, at placerat ligula nec mattis, in consequat sapien. Vivamus quis tincidunt mollis, mauris massa porttitor feugiat, ut sodales nibh lorem non nunc sed tempus.</p>
    <div class="author">
      <div class="avatar" role="img" aria-label="Portrait of the reviewer"></div>
      <b>LENA ORTIZ</b>
      <div class="dots"><i></i><i></i><i></i></div>
    </div>
  </div>
  <div class="login-panel">
    <div class="tabs"><span class="active">Sign In</span><span>Sign Up</span></div>
    <div class="field"><span>Account Type</span><span>▾</span></div>
    <div class="field"><span>User Name*</span></div>
    <div class="field"><span>Password*</span></div>
    <a class="btn" href="#">Log In</a>
  </div>
</section>

<section class="doctors">
  <h2 class="section-title">MEET OUR <strong>DOCTORS</strong></h2>
  <p class="section-lead">Lorem ipsum dolor sit amet, at placerat ligula nec mattis, in consequat sapien. Vivamus quis, tincidunt mollis, mauris massa porttitor feugiat.</p>
  <div class="doctor-row">
    <span class="slider-arrow" style="left:120px">‹</span>
    <div class="doctor-card">
      <div class="doctor-photo" role="img" aria-label="Photo of a doctor in a white coat"></div>
      <div class="doctor-info"><h3>DR OWEN HALE</h3><small>Cardiologist</small><div class="rating"><span class="stars">★★★★</span><span>25 Reviews</span></div></div>
    </div>
    <div class="doctor-card">
      <div class="doctor-photo" role="img" aria-label="Photo of a doctor with a stethoscope"></div>
      <div class="doctor-info"><h3>DR FELIX MARR</h3><small>Pediatrician</small><div class="rating"><span class="stars">★★★★</span><span>18 Reviews</span></div></div>
    </div>
    <div class="doctor-card">
      <div class="doctor-photo" role="img" aria-label="Photo of a doctor at a desk"></div>
      <div class="doctor-info"><h3>DR IRIS CALDER</h3><small>Dermatologist</small><div class="rating"><span class="stars">★★★★</span><span>31 Reviews</span></div></div>
    </div>
    <span class="slider-arrow" style="right:120px">›</span>
  </div>
  <a class="btn" href="#">Book An Appointment</a>
</section>

<div class="social-bar">
  <span>Get connected with us on social networks:</span>
  <div><i></i><i></i><i></i><i></i><i></i></div>
</div>

<footer class="site-footer">
  <div class="brand"><span class="brand-square"></span>CAREVIA</div>
  <div class="footer-col">
    <svg width="20" height="24" viewBox="0 0 20 24" fill="#fff"><path d="M10 0a9 9 0 0 0-9 9c0 7 9 15 9 15s9-8 9-15a9 9 0 0 0-9-9zm0 12a3 3 0 1 1 0-6 3 3 0 0 1 0 6z"/></svg>
    <h4>LOCATION</h4><p>27 Elmgrove Avenue,<br>Northbay NB 4021</p>
  </div>
  <div class="footer-col">
    <svg width="24" height="18" viewBox="0 0 24 18" fill="none" stroke="#fff" stroke-width="2"><rect x="1" y="1" width="22" height="16" rx="1"/><path d="M1 2l11 8 11-8"/></svg>
    <h4>EMAIL ADDRESS</h4><p>hello@carevia.example</p>
  </div>
  <div class="footer-col">
    <svg width="22" height="22" viewBox="0 0 24 24" fill="#fff"><path d="M6.6 10.8a15 15 0 0 0 6.6 6.6l2.2-2.2a1 1 0 0 1 1-.25 11.4 11.4 0 0 0 3.6.6 1 1 0 0 1 1 1V20a1 1 0 0 1-1 1A17 17 0 0 1 3 4a1 1 0 0 1 1-1h3.5a1 1 0 0 1 1 1c0 1.25.2 2.45.6 3.6a1 1 0 0 1-.25 1z"/></svg>
    <h4>CALL US</h4><p>+00 123 456 7890</p>
  </div>
</footer>

<div class="legal-bar">
  <span>© 2017 · All Rights Reserved</span>
  <nav><span>Terms and Conditions</span><span>Privacy Policy</span></nav>
</div>

</body>
</html>
```